Realty Group Needs Classy, Contemporary Letterhead Design

We need a letterhead design for a new realty company located in NY, USA. We buy investment properties to rehabilitate and or keep in our rental portfolio.

```html
<!DOCTYPE html>
<html lang="en">
<head>
<meta charset="utf-8">
<title>Halvern Realty Group — Letterhead</title>
<link href="https://fonts.googleapis.com/css2?family=Poppins:wght@400;500;700&family=Questrial&display=swap" rel="stylesheet">
<style>
  :root {
    --brand: #4b2a8a;
    --ink: #2b2b2b;
    --muted: #6b6b6b;
    --rule: #8a8a8a;
    --paper-light: #f3f3f3;
    --paper-dark: #e2e2e2;
    --sig-tone: #cfcfcf;
  }
  * { margin: 0; padding: 0; box-sizing: border-box; }
  html, body { width: 960px; height: 1200px; overflow: hidden; }
  body { background: var(--paper-dark); }
  .letterhead {
    position: relative;
    width: 960px;
    height: 1200px;
    background: linear-gradient(100deg, var(--paper-light) 0%, #e9e9e9 55%, var(--paper-dark) 100%);
    color: var(--ink);
    font-family: "Questrial", sans-serif;
  }
  .brand {
    position: absolute;
    left: 87px;
    top: 122px;
    display: flex;
    align-items: center;
    gap: 10px;
  }
  .brand-mark {
    width: 14px; height: 14px;
    background: var(--brand);
  }
  .brand-name {
    font-family: "Poppins", sans-serif;
    font-weight: 700;
    font-size: 21px;
    color: var(--brand);
    letter-spacing: 0.2px;
  }
  .address {
    position: absolute;
    left: 408px;
    top: 100px;
    font-family: "Poppins", sans-serif;
    font-size: 14px;
    line-height: 17px;
    color: var(--ink);
  }
  .address .web { color: var(--brand); font-weight: 500; }
  .contacts {
    position: absolute;
    left: 697px;
    top: 102px;
    list-style: none;
    font-family: "Poppins", sans-serif;
    font-size: 14px;
    line-height: 17px;
    color: var(--ink);
  }
  .contacts li { display: flex; align-items: center; gap: 6px; }
  .contacts svg { width: 10px; height: 10px; fill: var(--brand); }
  .header-rule {
    position: absolute;
    left: 87px; top: 163px;
    width: 792px; height: 1px;
    background: var(--rule);
  }
  .salutation {
    position: absolute;
    left: 87px; top: 350px;
    font-size: 22px;
  }
  .body-copy {
    position: absolute;
    left: 87px; top: 413px;
    width: 792px;
    font-size: 13.4px;
    line-height: 18.3px;
    text-align: justify;
    color: var(--ink);
  }
  .body-copy p { margin-bottom: 18.3px; }
  .closing {
    position: absolute;
    left: 87px; top: 798px;
    font-size: 13.4px;
  }
  .signature {
    position: absolute;
    left: 87px; top: 842px;
    width: 126px; height: 66px;
    background: linear-gradient(90deg, var(--sig-tone), #dadada);
    border-radius: 3px;
  }
  .footer-band {
    position: absolute;
    left: 0; bottom: 0;
    width: 960px; height: 14px;
    background: var(--brand);
  }
</style>
</head>
<body>
  <main class="letterhead">
    <header>
      <div class="brand">
        <span class="brand-mark"></span>
        <span class="brand-name">Halvern Realty Group, LLC</span>
      </div>
      <address class="address" style="font-style:normal">
        412 Linden Court<br>
        Albany, New York 12207<br>
        <span class="web">www.halvernrealty.com</span>
      </address>
      <ul class="contacts">
        <li>
          <svg viewBox="0 0 10 10" aria-hidden="true"><path d="M2 0.5 L3.6 0.5 L4.3 2.8 L3.2 3.7 C3.8 5 4.9 6.1 6.3 6.8 L7.2 5.7 L9.5 6.4 L9.5 8 C9.5 9 8.8 9.5 8 9.5 C4 9.3 0.7 6 0.5 2 C0.5 1.2 1 0.5 2 0.5 Z"/></svg>
          555-214-0387
        </li>
        <li>
          <svg viewBox="0 0 10 10" aria-hidden="true"><rect x="2.5" y="0.5" width="5" height="3"/><rect x="0.5" y="4" width="9" height="4" rx="1"/><rect x="2.5" y="7" width="5" height="2.5"/></svg>
          555-214-0390
        </li>
        <li>
          <svg viewBox="0 0 10 10" aria-hidden="true"><path d="M0.5 2 H9.5 V8.5 H0.5 Z M1.2 2.6 L5 5.5 L8.8 2.6 L8.8 3.3 L5 6.2 L1.2 3.3 Z" fill-rule="evenodd"/></svg>
          info@halvernrealty.com
        </li>
      </ul>
      <div class="header-rule"></div>
    </header>

    <p class="salutation">Dear Mr. Dalton,</p>

    <section class="body-copy">
      <p>Lorem ipsum dolor sit amet, consectetur adipiscing elit. Donec orci purus, luctus vitae dignissim eu, iaculis sed purus. Vivamus faucibus, ipsum nec aliquet viverra, leo mauris condimentum ligula, sit amet sagittis enim ligula quis arcu. Nam egestas tortor id nisi porttitor mattis. In tortor ante, ultricies in suscipit a, tempus non massa. Vivamus et auctor mi. Fusce vel massa nulla. Phasellus nec eros mauris, et scelerisque orci.</p>
      <p>Donec malesuada orci vitae nulla accumsan porta a id massa. Quisque accumsan iaculis magna sit amet fringilla. Maecenas consequat, magna eget tincidunt semper, odio nibh rutrum mi, id feugiat ante nisi eu risus. Vestibulum nunc orci, rhoncus a placerat in, ultricies in mi. Cras mattis varius eros, vel fringilla nisi suscipit eget. Quisque scelerisque sagittis nulla at porttitor.</p>
      <p>Sed id augue vitae urna euismod commodo aliquet a quam. Pellentesque arcu velit, cursus et malesuada ut, consequat et diam. Nullam erat sem, rhoncus id ullamcorper vitae, rhoncus et arcu. In ultricies ultricies nulla, ut rutrum nisi iaculis at. Donec eu magna a metus ornare faucibus. Fusce aliquet faucibus ultricies. Morbi semper, est id tincidunt gravida, sem arcu adipiscing lacus, ac bibendum nulla leo eu purus. Quisque nec diam sed risus consectetur a ccumsan quis quis nibh. Vestibulum id purus lorem.</p>
      <p>It is a long established fact that a reader will be distracted by the readable content of a page when looking at its layout. The point of using Lorem Ipsum is that it has a more-or-less normal distribution of letters, as opposed to using 'Content here, content here', making it look like readable English. Many desktop publishing packages</p>
    </section>

    <p class="closing">Sincerely,</p>
    <div class="signature" role="img" aria-label="Handwritten signature of the sender"></div>

    <div class="footer-band"></div>
  </main>
</body>
</html>
```